Energieberater sucht Flyer-Design
Zielgruppe
Ich bin Energieberater, habe mich vor kurzem selbstständig gemacht und möchte nun meine Bekanntheit steigern. Meine Zielgruppe sind Immobilieneigentümer sowie Immobiliensuchende, welchen ich eine fundierte Energieberatung mit Sanierungskonzepten sowie die Erstellung von Energieausweisen bieten kann.
Aufgabenstellung
Ich benötige einen Flyer, welchen ich regional verteilen möchte. Der Flyer soll quadratisch (148 x 148) erstellt werden.
Der Flyer sollte mein Logo, meine Kontaktdaten, die unten aufgeführten Dienstleistungen sowie einen Gutschein enthalten und insbesondere der Bekanntheits-/Imagesteigerung dienen.
Vorhandene Punkte sollen sein:
- Erstellung von Energieausweisen für Vermietung und Verkauf
- Energieberatung
- Sanierungs- und Modernisierungskonzepte
- Fördermittelberatung
Der Flyer soll die Möglichkeit bieten, am Rand abgeschnitten zu werden. Dort soll ein Gutschein aufgeführt werden mit 25 € Rabatt für einen Energieausweis.
Meine Kontaktdaten können Sie der angehängten Visitenkarte entnehmen.

```html
<!DOCTYPE html>
<html lang="de">
<head>
<meta charset="utf-8">
<title>Energieberatung Jonas Wendel – Flyer</title>
<link rel="stylesheet" href="https://fonts.googleapis.com/css2?family=Arimo:wght@400;700&family=Roboto:wght@300;700;900&display=swap">
<style>
  :root {
    --teal: #117b99;
    --ink: #4b4b4b;
    --paper: #ffffff;
    --backdrop: #e8e8e8;
  }
  * { margin: 0; padding: 0; box-sizing: border-box; }
  html, body { width: 1200px; height: 735px; overflow: hidden; }
  body { background: var(--backdrop); font-family: "Arimo", Arial, sans-serif; color: var(--ink); position: relative; }

  .flyer { position: absolute; left: 335px; top: 103px; width: 530px; height: 530px; background: var(--paper); }
  .flyer > * { position: absolute; }

  .top-bar { left: 23px; top: 0; width: 194px; height: 11px; background: var(--teal); }

  .brand { left: 23px; top: 18px; width: 194px; height: 40px; display: flex; align-items: center; gap: 8px; }
  .brand-dot { width: 26px; height: 26px; border-radius: 50%; background: var(--teal); flex: none; }
  .brand-name { color: var(--teal); font-size: 10px; line-height: 12px; letter-spacing: 0.9px; text-transform: uppercase; }

  .info-box { position: absolute; height: 38px; border: 1.3px solid var(--teal); text-align: center; font-size: 12.5px; color: var(--ink); padding-top: 14px; white-space: nowrap; }
  .info-box.address { left: 23px; top: 73px; width: 188px; }
  .badge { position: absolute; left: 50%; top: -14px; width: 26px; height: 26px; margin-left: -13px; border-radius: 50%; background: var(--teal); display: flex; align-items: center; justify-content: center; }

  .divider { left: 23px; top: 123px; width: 194px; height: 1.3px; background: var(--teal); }

  .services { left: 0; top: 142px; width: 233px; text-align: center; list-style: none; font-size: 15px; line-height: 16.5px; }
  .services li + li::before { content: ""; display: block; width: 19px; height: 1.3px; background: var(--teal); margin: 11px auto 12px; }

  .photo { left: 233px; top: 0; width: 297px; height: 361px; background: linear-gradient(135deg, #e6ecf5 0%, #d4deec 45%, #e9d6c8 75%, #d9a24c 100%); }

  .coupon { left: 0; top: 361px; width: 296px; height: 169px; background: var(--teal); color: #fff; font-family: "Roboto", Arial, sans-serif; }
  .coupon-frame { position: absolute; left: 15px; top: 29px; width: 263px; height: 115px; border: 1.6px solid #fff; }
  .coupon-amount { position: absolute; left: 76px; top: 10px; width: 145px; background: var(--teal); text-align: center; font-weight: 900; font-size: 76px; line-height: 64px; letter-spacing: -2px; }
  .coupon-label { position: absolute; left: 0; top: 74px; width: 296px; text-align: center; line-height: 28px; }
  .coupon-label .light { font-weight: 300; font-size: 26px; letter-spacing: 0.6px; display: block; }
  .coupon-label .bold { font-weight: 700; font-size: 25px; display: block; }

  .contact { left: 296px; top: 361px; width: 234px; height: 169px; }
  .contact .info-box { left: 19px; width: 194px; }
  .contact .phone { top: 29px; font-size: 13.5px; padding-top: 15px; }
  .contact .email { top: 82px; font-size: 11px; padding-top: 17px; }
  .web-bar { position: absolute; left: 19px; top: 134px; width: 194px; height: 11px; background: var(--teal); color: #fff; font-size: 8.5px; line-height: 11px; text-align: center; }
</style>
</head>
<body>
  <div class="flyer">
    <div class="top-bar"></div>

    <div class="brand">
      <span class="brand-dot"></span>
      <span class="brand-name">Energieberatung<br>Jonas Wendel</span>
    </div>

    <div class="info-box address">
      <span class="badge">
        <svg width="14" height="16" viewBox="0 0 14 16" fill="none" stroke="#fff" stroke-width="1.4"><path d="M7 15s5-5 5-8.5A5 5 0 0 0 2 6.5C2 10 7 15 7 15z"/><circle cx="7" cy="6.5" r="1.8"/></svg>
      </span>
      Am Lindenhang | 35210 Talbach
    </div>

    <div class="divider"></div>

    <ul class="services">
      <li>Sanierungs- und<br>Modernisierungskonzepte</li>
      <li>Erstellung von Energieaus-<br>weisen für Vermietung<br>und Verkauf</li>
      <li>Fördermittelberatung</li>
      <li>Energieberatung</li>
    </ul>

    <div class="photo" role="img" aria-label="Foto: Hausmodell mit rotem Dach auf Bauplänen neben farbiger Energieeffizienzskala A bis G"></div>

    <div class="coupon">
      <div class="coupon-frame"></div>
      <div class="coupon-amount">25 €</div>
      <div class="coupon-label">
        <span class="light">RABATT FÜR IHREN</span>
        <span class="bold">ENERGIEAUSWEIS</span>
      </div>
    </div>

    <div class="contact">
      <div class="info-box phone">
        <span class="badge">
          <svg width="14" height="14" viewBox="0 0 14 14" fill="none" stroke="#fff" stroke-width="1.3" stroke-linejoin="round"><path d="M3 1.5l2 2.5-1.2 1.5a8 8 0 0 0 4.7 4.7L10 9l2.5 2-1 1.8C6 13 1 8 1.2 2.5z"/></svg>
        </span>
        +49 0151 48207315
      </div>
      <div class="info-box email">
        <span class="badge">
          <svg width="14" height="11" viewBox="0 0 14 11" fill="none" stroke="#fff" stroke-width="1.3"><rect x="1" y="1" width="12" height="9"/><path d="M1 1l6 5 6-5"/></svg>
        </span>
        info@energieberatung-wendel.com
      </div>
      <div class="web-bar">www.energieberatung-wendel.com</div>
    </div>
  </div>
</body>
</html>
```